motorhome needs a name at the front to make it ours

Need a sign to put on front of our motorhome we are about to live in indefinitely. Will be travelling and working all over Australia. The area will be about 2m wide by 1m high.

I am the bohemian, a young minded, fit and healthy 50 year old. I'm a medical administrator and a travelling massage therapist. I love travel, music, mountains, oceans, exercise and white wine.

My husband is very hard working in civil construction (earthworks) and an avid lawn bowler. He loves beer, tv, fishing.

We both love being together but also thoroughly enjoy being with friends.

Sans Serif

• The Stargazer and The Tinkerer or around the other way
• If I could design I would make the "o" in bohemian a peace sign or very flowery or a dream catcher and I would make the "o" in bowler to look like a lawn bowl but this is not essential if you have a different idea. Looking forward to seeing what you clever people can do for me.
• Nothing to include here

```html
<!DOCTYPE html>
<html lang="en">
<head>
<meta charset="utf-8">
<title>The Stargazer and The Tinkerer – Motorhome Sign</title>
<link href="https://fonts.googleapis.com/css2?family=Exo+2:ital,wght@1,800;1,900&family=Dancing+Script:wght@700&display=swap" rel="stylesheet">
<style>
  :root {
    --page: #e9e9e7;
    --sign-black: #0d0d0f;
    --sign-map: #1c1d21;
    --sign-edge: #f4f4f4;
    --pink: #ef4f8b;
    --pink-soft: #f27aa6;
    --silver-light: #f2f2f2;
    --silver-mid: #b9bcc1;
    --silver-dark: #7d8187;
    --white: #ffffff;
    --photo-warm: #9a7a5c;
    --photo-cool: #5b6470;
  }
  * { margin: 0; padding: 0; box-sizing: border-box; }
  html, body {
    width: 900px;
    height: 1200px;
    overflow: hidden;
    background: var(--page);
  }
  .canvas {
    position: relative;
    width: 900px;
    height: 1200px;
  }
  .sign {
    position: absolute;
    left: 20px;
    top: 377px;
    width: 860px;
    height: 446px;
    background: var(--sign-black);
    border: 4px solid var(--sign-edge);
    overflow: hidden;
  }
  .sign__map {
    position: absolute;
    inset: 0;
    background: radial-gradient(ellipse at 45% 55%, var(--sign-map) 0%, var(--sign-black) 75%);
  }
  .sign__route {
    position: absolute;
    inset: 0;
  }
  .sign__the {
    position: absolute;
    left: 26px;
    top: 112px;
    font-family: "Dancing Script", cursive;
    font-weight: 700;
    font-size: 44px;
    line-height: 1;
    color: var(--pink);
  }
  .sign__first-name {
    position: absolute;
    left: 112px;
    top: 62px;
    font-family: "Exo 2", sans-serif;
    font-style: italic;
    font-weight: 900;
    font-size: 108px;
    line-height: 1;
    letter-spacing: -1px;
    color: var(--pink);
  }
  .sign__joiner {
    position: absolute;
    left: 182px;
    top: 252px;
    font-family: "Dancing Script", cursive;
    font-weight: 700;
    font-size: 30px;
    line-height: 1;
    color: var(--white);
  }
  .sign__second-name {
    position: absolute;
    left: 300px;
    top: 160px;
    font-family: "Exo 2", sans-serif;
    font-style: italic;
    font-weight: 900;
    font-size: 116px;
    line-height: 1;
    letter-spacing: -1px;
    background: linear-gradient(180deg, var(--silver-light) 0%, var(--silver-mid) 55%, var(--silver-dark) 100%);
    -webkit-background-clip: text;
    background-clip: text;
    color: transparent;
  }
  .sign__photo {
    position: absolute;
    left: 0;
    top: 332px;
    width: 262px;
    height: 110px;
    background: linear-gradient(135deg, var(--photo-warm) 0%, var(--photo-cool) 100%);
  }
  .sign__vehicle {
    position: absolute;
    left: 688px;
    top: 292px;
    width: 130px;
    height: 62px;
    background: var(--pink);
    border-radius: 10px;
  }
</style>
</head>
<body>
  <main class="canvas">
    <section class="sign" aria-label="Motorhome sign: The Stargazer and The Tinkerer">
      <div class="sign__map" role="img" aria-label="Faint dark map of Australia with state and city names"></div>
      <svg class="sign__route" width="852" height="438" viewBox="0 0 852 438" aria-hidden="true">
        <path d="M28 278 C 100 320, 200 336, 330 334 S 560 326, 686 322"
              fill="none" stroke="var(--pink-soft)" stroke-width="4"
              stroke-dasharray="2 9" stroke-linecap="round"/>
      </svg>
      <span class="sign__the">The</span>
      <h1 class="sign__first-name">Stargazer</h1>
      <span class="sign__joiner">and the</span>
      <h2 class="sign__second-name">Tinkerer</h2>
      <div class="sign__photo" role="img" aria-label="Photo of the couple in beanies and sunglasses"></div>
      <div class="sign__vehicle" role="img" aria-label="Pink motorhome illustration at the end of the route"></div>
    </section>
  </main>
</body>
</html>
```